PPT Template for a company that develops software and intellectual property for use by accountants a

We are a boutique firm that develops specialised reporting applications, financial and non-financial reporting content, checklists and other intellectual property for use by business consultants and accounting firms in particular. The applications and content we are creating is strategically focussed and we are required to produce reports and presentations and our current templates are simply not sufficient.

Excel worksheets, graphs and other graphics are regularly embedded into the presentations
We have our logo in 4 colour palettes and will require the winning version to be provided in all 4 colours plus B&W. There is one single logo but the name “Lantern Trade Pathfinders” is presented in 3 different styles for use depending on the space available etc.
Our clients will typically take our products and rebrand/co brand these (we require them to at least say that there product is “powered by Lantern Trade Pathfinders” with the logo.
The templates you provide will be used to create marketing presentations, proposal presentations and our standard documents that clients will rebrand or cobrand under license.

A Powerpoint Document Slide Template

Cover page layout, back page, intermediate page heading, in colours and styles based on the logo, title styles, and an intermediate or chapter heading slide style. Many of our presentations contain slides with tables, diagrams, flowcharts and text, including simple lists of bullet points. As above, you will see in our style guide that we have four coloured logos – we would like one version in each. We recommend that we finalise the design using the maroon version and then this be used as the base for the other colour palettes.
Again, the cover should be bold and draw attention but remain professional.

We are looking for something that works in both 4:3 and 16:9 (or two templates please)

We like a clear professional and simple look.

Deliverable: PowerPoint template file (.potx extension) for PowerPoint 2007 with at least a “cover” layout, a “title and content” layout, and a simplified slide layout, as well as “back cover”. Please embed any fonts used.

Industry/Entity Type

Financial

```html
<!DOCTYPE html>
<html lang="en">
<head>
<meta charset="utf-8">
<title>Project Title Here</title>
<link rel="stylesheet" href="https://fonts.googleapis.com/css2?family=Ubuntu:wght@400;500;700&display=swap">
<style>
  :root {
    --brand-orange: #f47320;
    --brand-peach: #ff9a5a;
    --grey-light: #c0c0c0;
    --grey-mid: #808080;
    --grey-dark: #5a5a5a;
    --ink: #1a1a1a;
    --paper: #ffffff;
  }
  * { margin: 0; padding: 0; box-sizing: border-box; }
  html, body { width: 1200px; height: 900px; overflow: hidden; background: var(--paper); }
  body { font-family: "Ubuntu", Arial, sans-serif; color: var(--ink); }
  .slide { position: relative; width: 1200px; height: 900px; background: var(--paper); }

  .slide-header {
    position: absolute; left: 0; top: 0; width: 1200px; height: 86px;
    background: var(--brand-orange);
    display: flex; align-items: center; justify-content: space-between;
    padding: 0 24px 0 20px;
  }
  .slide-title { color: var(--paper); font-size: 48px; font-weight: 500; letter-spacing: 0.5px; }
  .brand-name { color: var(--paper); font-size: 18px; font-weight: 500; }

  .content { position: absolute; left: 72px; top: 276px; width: 560px; }
  .content-subtitle { color: var(--brand-orange); font-size: 26px; font-weight: 700; margin-bottom: 12px; }
  .content-paragraph { font-size: 20.5px; line-height: 36px; margin-bottom: 36px; }

  .pie-chart { position: absolute; left: 680px; top: 298px; }
  .pie-label { font-family: "Ubuntu", Arial, sans-serif; font-size: 17px; font-weight: 500; text-anchor: middle; }
  .pie-label--dark { fill: var(--ink); }
  .pie-label--light { fill: var(--paper); }

  .slide-footer {
    position: absolute; left: 0; bottom: 0; width: 1200px; height: 50px;
    background: var(--brand-orange); color: var(--paper);
    display: flex; align-items: center; justify-content: space-between;
    padding: 0 12px 0 14px; font-size: 18px;
  }
</style>
</head>
<body>
<div class="slide">
  <header class="slide-header">
    <h1 class="slide-title">PROJECT TITLE HERE</h1>
    <span class="brand-name">Lantern Trade Pathfinders</span>
  </header>

  <section class="content">
    <h2 class="content-subtitle">PARAGRAPH SUB TITLE</h2>
    <p class="content-paragraph">Lorem ipsum dolor sit ipsum Lorem ipsum dolor sit ipsum Lorem ipsum Lorem ipsum dolor sit ipsum Lorem ipsum dolor sit ipsum Lorem ipsum Lorem ipsum dolor sit ipsum Lorem ipsum dolor sit ipsum</p>
    <p class="content-paragraph">Lorem ipsum Lorem ipsum dolor sit ipsum Lorem ipsum dolor sit ipsum Lorem ipsum</p>
    <p class="content-paragraph">Lorem ipsum dolor sit ipsum Lorem ipsum dolor sit ipsum Lorem ipsum Lorem ipsum dolor sit ipsum Lorem ipsum dolor sit ipsum Lorem ipsum Lorem ipsum dolor sit ipsum Lorem ipsum dolor sit ipsum Lorem ipsum</p>
  </section>

  <svg class="pie-chart" width="480" height="480" viewBox="676 294 480 480" role="img" aria-label="Pie chart with five segments">
    <g stroke="#ffffff" stroke-width="2">
      <path d="M916 534 L916 304 A230 230 0 0 1 1050.3 347.2 Z" fill="var(--grey-light)"/>
      <path d="M916 534 L1050.3 347.2 A230 230 0 0 1 1133.5 608.9 Z" fill="var(--brand-orange)"/>
      <path d="M916 534 L1133.5 608.9 A230 230 0 0 1 698.5 608.9 Z" fill="var(--brand-peach)"/>
      <path d="M916 534 L698.5 608.9 A230 230 0 0 1 784.1 345.6 Z" fill="var(--grey-dark)"/>
      <path d="M916 534 L784.1 345.6 A230 230 0 0 1 916 304 Z" fill="var(--grey-mid)"/>
    </g>
    <text class="pie-label pie-label--dark" x="961" y="369"><tspan x="961">Lorem</tspan><tspan x="961" dy="22">ipsum</tspan><tspan x="961" dy="22">dolor</tspan></text>
    <text class="pie-label pie-label--light" x="871" y="369"><tspan x="871">Lorem</tspan><tspan x="871" dy="22">ipsum</tspan><tspan x="871" dy="22">dolor</tspan></text>
    <text class="pie-label pie-label--dark" x="1054" y="502"><tspan x="1054">Lorem ipsum</tspan><tspan x="1054" dy="23">dolor</tspan></text>
    <text class="pie-label pie-label--light" x="787" y="494"><tspan x="787">Lorem ipsum dolor</tspan><tspan x="787" dy="23">Lorem ipsum dolor</tspan></text>
    <text class="pie-label pie-label--dark" x="921" y="643"><tspan x="921">Lorem ipsum dolor</tspan><tspan x="921" dy="23">Lorem ipsum dolor</tspan></text>
    <circle cx="916" cy="534" r="36" fill="var(--brand-orange)" stroke="#ffffff" stroke-width="5"/>
  </svg>

  <footer class="slide-footer">
    <span class="footer-copyright">Copyright text here</span>
    <span class="footer-page">Page : 01</span>
  </footer>
</div>
</body>
</html>
```